Real Estate Investor needs awesome business card design

I invest in real estate, focused on multi-family properties, and I need a business card to hand out to potential partners. I prefer simple, clean designs, but it needs to stand out, so I'd like there to be a bit of red in the design as well.

It should include this information:

Front
Dallin Pecksworth
Real Estate Investor
Direct phone: 502-867-3394
Email: dallinhpecksworth@quillmail.example
Headshot (Picture), I've uploaded a few, just pick the one you think looks best with your design. You can remove the background from the headshot image if it looks better.

Back
The back of the card's design should flow and be congruent with the front. On the back I want to put an inspirational quote or question. There will be different ones depending on the card, so I'll need the original file so I can edit it in the end.

For now, use “The Pessimist Sees Difficulty In Every Opportunity. The Optimist Sees The Opportunity In Every Difficulty.” -Barnaby Ellsworth

Target Market(s)

Investors

Industry/Entity Type

Real Estate

Contact Information for Business Card

Front
Dallin Pecksworth
Real Estate Investor

Back
The back of the card's design should flow and be congruent with the front. On the back I want to put an inspirational quote or question. There will be different ones depending on the card, so I'll need the original file so I can edit it in the end. I've uploaded some EXAMPLES of business cards with quotes on them. Don't copy but feel free to use them as inspiration.

The design will be printed on "ZIB sized" business cards
1039 x 697 pixels
with rounded corners

Font styles to use
Serif
Decorative
Script

Colors
ec1f27

Requirements
Must have
• Headshot, name, and other information in it.
• 1039 x 697 pixels
• Rounded corners
• Clean design that pops. I'm open to see any color background, including black.
• Headshots can be located here: https://www.filecrate.example/sh/8kd2wq7mzt31hvx/BBQTXP4ruf9LmQ0KhcvWx7b?dl=0
Nice to have
• It would be awesome if the design included a personal signature or monogram, but if not I'll get a personal logo developed later and the card redesigned if I think it needs it.
Should not have
• Cluttered design

```html
<!DOCTYPE html>
<html lang="en">
<head>
<meta charset="utf-8">
<title>Dallin Pecksworth – Business Card</title>
<link rel="stylesheet" href="https://fonts.googleapis.com/css2?family=Open+Sans:wght@300;400;600&family=Kalam:wght@300&family=Playfair+Display:wght@900&display=swap">
<style>
  :root {
    --canvas: #d6d6d6;
    --card: #2a2a2c;
    --card-edge: #232325;
    --red: #ec1f27;
    --text-light: #e6e6e6;
    --text-muted: #a4a4a6;
    --photo-light: #5a5a5d;
    --photo-dark: #2a2a2c;
  }
  * { margin: 0; padding: 0; box-sizing: border-box; }
  html, body { width: 1200px; height: 1200px; overflow: hidden; background: var(--canvas); }
  body { position: relative; font-family: "Open Sans", Arial, sans-serif; }

  .card {
    position: absolute;
    left: 220px;
    width: 760px;
    height: 510px;
    background: var(--card);
    border-radius: 22px;
    overflow: hidden;
    box-shadow: 0 10px 30px rgba(0,0,0,0.25);
  }
  .card--front { top: 60px; }
  .card--back { top: 630px; }

  .headshot { position: absolute; left: 0; top: 0; width: 760px; height: 510px; }
  .accent-lines { position: absolute; left: 0; top: 0; width: 760px; height: 510px; }

  .identity { position: absolute; left: 72px; top: 262px; }
  .identity__name {
    font-size: 29px; font-weight: 400; letter-spacing: 6px;
    color: var(--text-light); text-transform: uppercase; white-space: nowrap;
  }
  .identity__name .surname { color: var(--red); }
  .identity__title { margin-top: 4px; font-size: 13px; font-weight: 300; color: var(--text-muted); }

  .contacts { position: absolute; left: 76px; top: 332px; list-style: none; }
  .contacts__item {
    display: flex; align-items: center; gap: 10px;
    font-size: 13px; font-weight: 300; color: var(--text-muted);
    margin-bottom: 10px; white-space: nowrap;
  }
  .contacts__icon { width: 12px; height: 12px; fill: var(--text-muted); }

  .quote {
    position: absolute; left: 130px; top: 170px; width: 520px;
    font-family: "Kalam", "Comic Sans MS", cursive;
    font-weight: 300; font-style: italic;
    font-size: 21px; line-height: 1.45; color: var(--text-light);
  }
  .quote__mark {
    position: absolute;
    font-family: "Playfair Display", Georgia, serif;
    font-weight: 900; font-size: 110px; line-height: 1;
    color: var(--red);
  }
  .quote__mark--open { left: 70px; top: 250px; }
  .quote__mark--close { left: 640px; top: 120px; }
  .quote__author {
    position: absolute; left: 460px; top: 268px;
    font-family: "Open Sans", Arial, sans-serif;
    font-size: 11px; letter-spacing: 4px; text-transform: uppercase;
    color: var(--text-muted);
  }
</style>
</head>
<body>

<section class="card card--front">
  <svg class="headshot" viewBox="0 0 760 510" role="img" aria-label="Black and white headshot of Dallin Pecksworth in a dark blazer, with his personal signature">
    <defs>
      <radialGradient id="headshotTone" cx="0.55" cy="0.35" r="0.7">
        <stop offset="0" stop-color="var(--photo-light)"/>
        <stop offset="1" stop-color="var(--photo-dark)"/>
      </radialGradient>
    </defs>
    <polygon points="440,0 760,0 760,300 440,390" fill="url(#headshotTone)"/>
  </svg>

  <div class="identity">
    <h1 class="identity__name">Dallin <span class="surname">Pecksworth</span></h1>
    <p class="identity__title">Real Estate Investor</p>
  </div>

  <ul class="contacts">
    <li class="contacts__item">
      <svg class="contacts__icon" viewBox="0 0 24 24"><path d="M6.6 10.8a15.1 15.1 0 0 0 6.6 6.6l2.2-2.2a1 1 0 0 1 1-.25 11.4 11.4 0 0 0 3.6.57 1 1 0 0 1 1 1V20a1 1 0 0 1-1 1A17 17 0 0 1 3 4a1 1 0 0 1 1-1h3.5a1 1 0 0 1 1 1c0 1.25.2 2.45.57 3.57a1 1 0 0 1-.25 1z"/></svg>
      502-867-3394
    </li>
    <li class="contacts__item">
      <svg class="contacts__icon" viewBox="0 0 24 24"><path d="M2 5h20v14H2z M2 5l10 8 10-8" fill="none" stroke="var(--text-muted)" stroke-width="2.4"/></svg>
      dallinhpecksworth@quillmail.example
    </li>
  </ul>

  <svg class="accent-lines" viewBox="0 0 760 510" aria-hidden="true">
    <g stroke="var(--red)" fill="none" stroke-linecap="round">
      <line x1="60" y1="510" x2="760" y2="296" stroke-width="4"/>
      <line x1="140" y1="510" x2="760" y2="318" stroke-width="3"/>
      <line x1="40" y1="500" x2="760" y2="350" stroke-width="3"/>
      <line x1="250" y1="510" x2="760" y2="372" stroke-width="3"/>
      <line x1="380" y1="468" x2="760" y2="470" stroke-width="3"/>
    </g>
  </svg>
</section>

<section class="card card--back">
  <span class="quote__mark quote__mark--open" aria-hidden="true">&ldquo;</span>
  <blockquote class="quote">
    The Pessimist Sees Difficulty In Every Opportunity.<br>
    The Optimist Sees The Opportunity In Every Difficulty.
  </blockquote>
  <span class="quote__mark quote__mark--close" aria-hidden="true">&rdquo;</span>
  <p class="quote__author">- Barnaby Ellsworth</p>
</section>

</body>
</html>
```